New Web Design Project

Require a website for The Bramwell Harvest. All relevant information is in the uploaded files.

website to be responsive to work on mobile.

Required in html5, css

Coding

Coded - Design and coding required

Number of Pages Required

3 page

```html
<!DOCTYPE html>
<html lang="en">
<head>
<meta charset="utf-8">
<meta name="viewport" content="width=device-width, initial-scale=1">
<title>The Bramwell Harvest — Fresh Produce Trading Consultancy</title>
<link rel="stylesheet" href="https://fonts.googleapis.com/css2?family=Montserrat:wght@300;400;500;600;700;800&family=Open+Sans:wght@400;600&display=swap">
<style>
  :root {
    --green: #8cc63f;
    --orange: #f26f1c;
    --orange-light: #f7892d;
    --dark: #1e1e1e;
    --ink: #1a1a1a;
    --text: #3a3a3a;
    --muted: #4a4a4a;
    --panel: #f5f5f5;
    --white: #ffffff;
    --footer: #000000;
  }
  * { box-sizing: border-box; margin: 0; padding: 0; }
  html, body { width: 1200px; height: 2745px; overflow: hidden; }
  body { font-family: "Open Sans", Arial, sans-serif; color: var(--text); background: var(--white); position: relative; }
  .abs { position: absolute; }

  /* Header + hero */
  .hero { position: absolute; left: 0; top: 0; width: 1200px; height: 725px; overflow: hidden; }
  .hero-photo { position: absolute; inset: 0; background: radial-gradient(ellipse at 60% 45%, #5a5a5a 0%, #3a3a3a 40%, #242424 75%, #1c1c1c 100%); }
  .brand { position: absolute; left: 113px; top: 28px; display: flex; align-items: center; gap: 10px; font-family: "Montserrat", sans-serif; font-weight: 700; font-size: 24px; color: var(--white); }
  .brand-dot { width: 22px; height: 22px; border-radius: 50%; background: var(--green); }
  .nav { position: absolute; top: 37px; left: 574px; display: flex; align-items: center; font-family: "Montserrat", sans-serif; font-weight: 600; font-size: 13px; color: var(--white); }
  .nav a { color: inherit; text-decoration: none; position: relative; }
  .nav .sep { width: 1px; height: 12px; background: rgba(255,255,255,0.55); margin: 0 30px; }
  .nav .active::after { content: ""; position: absolute; left: 0; right: 0; top: 28px; height: 3px; background: var(--green); border-radius: 2px; }
  .hero-kicker { position: absolute; left: 113px; top: 266px; font-family: "Montserrat", sans-serif; font-weight: 400; font-size: 32px; letter-spacing: 4px; color: var(--white); }
  .bar { position: absolute; height: 3px; background: var(--green); }
  .hero-title { position: absolute; left: 113px; top: 334px; font-family: "Montserrat", sans-serif; font-weight: 800; font-size: 54px; line-height: 54px; color: var(--white); }
  .play { position: absolute; left: 806px; top: 468px; }

  /* About */
  .about { position: absolute; left: 0; top: 725px; width: 1200px; height: 672px; background: var(--white); }
  .about-art { position: absolute; left: 0; top: 0; }
  .section-title { font-family: "Montserrat", sans-serif; font-weight: 700; color: var(--ink); position: absolute; }
  .about-title { left: 646px; top: 124px; font-size: 42px; }
  .about-copy { position: absolute; left: 646px; top: 213px; width: 520px; font-size: 15.5px; line-height: 27px; color: var(--text); }
  .about-copy p + p { margin-top: 29px; }

  /* People */
  .people { position: absolute; left: 0; top: 1397px; width: 1200px; height: 627px; background: var(--panel); }
  .people-title { left: 0; width: 1200px; text-align: center; top: 70px; font-size: 38px; }
  .person { position: absolute; top: 218px; }
  .portrait { position: absolute; left: 0; top: 26px; width: 188px; height: 188px; border-radius: 50%; background: radial-gradient(circle at 50% 40%, #9bd24a 0%, var(--green) 60%, #6fae2b 100%); }
  .person-info { position: absolute; left: 225px; top: 22px; width: 280px; }
  .person-name { font-family: "Montserrat", sans-serif; font-weight: 700; font-size: 17px; color: #2a2a2a; }
  .person-role { font-family: "Montserrat", sans-serif; font-weight: 400; font-size: 18px; color: var(--muted); margin-top: 2px; }
  .person-bio { font-size: 12.2px; line-height: 20.3px; color: var(--muted); margin-top: 12px; }

  /* Contact */
  .contact { position: absolute; left: 0; top: 2024px; width: 1200px; height: 618px; overflow: hidden; }
  .contact-photo { position: absolute; inset: 0; background: linear-gradient(180deg, var(--orange) 0%, var(--orange-light) 50%, #f27a22 75%, var(--orange) 100%); }
  .contact-title { left: 613px; top: 80px; font-size: 38px; color: var(--white); }
  .field { position: absolute; left: 611px; width: 467px; height: 46px; border-radius: 23px; background: var(--white); font-family: "Montserrat", sans-serif; font-size: 11.5px; color: #333; padding: 16px 22px; }
  .field.message { height: 110px; border-radius: 20px; padding: 12px 19px; }
  .send { position: absolute; left: 615px; top: 2479px; width: 172px; height: 48px; border-radius: 24px; background: var(--green); color: var(--white); font-family: "Montserrat", sans-serif; font-weight: 600; font-size: 14px; display: flex; align-items: center; justify-content: center; }

  /* Footer */
  .footer { position: absolute; left: 0; top: 2642px; width: 1200px; height: 103px; background: var(--footer); }
  .footer .brand { left: 120px; top: 38px; font-size: 22px; }
  .copyright { position: absolute; left: 406px; top: 44px; font-family: "Montserrat", sans-serif; font-size: 12.5px; color: var(--white); }
  .social { position: absolute; left: 939px; top: 36px; display: flex; gap: 6px; }
  .social span { width: 32px; height: 32px; border-radius: 50%; border: 1.5px solid var(--white); }
</style>
</head>
<body>

<header class="hero">
  <div class="hero-photo" role="img" aria-label="Monochrome city skyline across the water at dusk"></div>
  <div class="brand"><span class="brand-dot"></span>The Bramwell Harvest</div>
  <nav class="nav">
    <a class="active">HOME</a><span class="sep"></span>
    <a>ABOUT US</a><span class="sep"></span>
    <a>SERVICES</a><span class="sep"></span>
    <a>PEOPLE</a><span class="sep"></span>
    <a>CONTACT US</a>
  </nav>
  <div class="hero-kicker">THE BRAMWELL HARVEST</div>
  <div class="bar" style="left:116px; top:311px; width:51px;"></div>
  <h1 class="hero-title">FRESH PRODUCE<br>TRADING<br>CONSULTANCY</h1>
  <svg class="play" width="92" height="92" viewBox="0 0 92 92" aria-label="Play video">
    <circle cx="46" cy="46" r="41" fill="none" stroke="#fff" stroke-width="6"/>
    <path d="M36 27 L66 46 L36 65 Z" fill="#fff"/>
  </svg>
</header>

<section class="about">
  <svg class="about-art" width="620" height="672" viewBox="0 0 620 672">
    <defs>
      <linearGradient id="lineFill" x1="0" y1="0" x2="0" y2="1">
        <stop offset="0" stop-color="#2d4f8f"/>
        <stop offset="0.45" stop-color="#3a5ea6"/>
        <stop offset="0.6" stop-color="#e6c21a"/>
        <stop offset="0.8" stop-color="#f2c60c"/>
        <stop offset="1" stop-color="#1d2d55"/>
      </linearGradient>
    </defs>
    <path role="img" aria-label="Bottling line with rows of orange juice bottles in a factory" d="M0 0 H488 C600 120 610 460 350 672 H0 Z" fill="url(#lineFill)"/>
    <path d="M492 0 C610 120 625 460 352 672" fill="none" stroke="#8cc63f" stroke-width="7"/>
  </svg>
  <h2 class="section-title about-title">ABOUT US</h2>
  <div class="bar" style="left:650px; top:181px; width:48px;"></div>
  <div class="about-copy">
    <p>The Bramwell Harvest was incorporated with the objective of introducing new vendors to the Canadian market through a trusted and mutual business relation It was set up by Omar Valdane and Dario Kostelec who have a combined experience of over 45 years in the fresh produce business. With Omar's expertise in global sourcing and Dario's vast connection and know how of the Canadian market, we have helped our existing partners grow and expand their reach in the Canadian fresh produce market.</p>
    <p>Our expertise and supply chain knowledge allow us to develop programs and introduce new products to the Canadian consumer, via retail and wholesale channels across Canada. Get in touch to discuss how we can add value to your business</p>
  </div>
</section>

<section class="people">
  <h2 class="section-title people-title">OUR PEOPLE</h2>
  <div class="bar" style="left:579px; top:125px; width:52px;"></div>

  <article class="person" style="left:78px;">
    <div class="portrait" role="img" aria-label="Portrait of Dario Kostelec, founder"></div>
    <div class="person-info">
      <div class="person-name">DARIO KOSTELEC</div>
      <div class="person-role">Founder</div>
      <p class="person-bio">Dario is a detail oriented manager &amp; a leader who closely watches the P&amp;L but never loses sight of the strategic perspective. I have worked with Dario for about 5 years &amp; I always found him to be a great leader with a strong motivational force to run a large &amp; a diverse group of sales and operational teams located at multiple locations across Canada &amp; US.</p>
    </div>
  </article>

  <article class="person" style="left:628px;">
    <div class="portrait" role="img" aria-label="Portrait of Omar Valdane, founder and president"></div>
    <div class="person-info">
      <div class="person-name">OMAR VALDANE</div>
      <div class="person-role">Founder &amp; President</div>
      <p class="person-bio">Omar is a detail oriented manager &amp; a leader who closely watches the P&amp;L but never loses sight of the strategic perspective. I have worked with Omar for about 5 years &amp; I always found him to be a great leader with a strong motivational force to run a large &amp; a diverse group of sales and operational teams located at multiple locations across Canada &amp; US.</p>
    </div>
  </article>
</section>

<section class="contact">
  <div class="contact-photo" role="img" aria-label="City skyline at sunset washed in orange"></div>
  <h2 class="section-title contact-title">CONTACT US</h2>
  <div class="bar" style="left:617px; top:135px; width:53px; background:#fff;"></div>
</section>
<div class="field" style="top:2182px;">Your Name *</div>
<div class="field" style="top:2237px;">Phone *</div>
<div class="field" style="top:2295px;">Email address*</div>
<div class="field message" style="top:2353px;">Write Your Message</div>
<div class="send">SEND MESSAGE</div>

<footer class="footer">
  <div class="brand"><span class="brand-dot"></span>The Bramwell Harvest</div>
  <div class="copyright">Copyright © 2010-2020 The Bramwell Harvest All rights reserved.</div>
  <div class="social" aria-label="Social links"><span></span><span></span><span></span><span></span></div>
</footer>

</body>
</html>
```